Handy man Company business card

need branded business card for my new company, this design will transfer to car wrap design what winner will be asked to design

I will need original file so I can edit it in the end.

Also like to have some inspirational quote like "ONE CALL WE DO IT ALL"
"We do it right" can be added to logo side

Like to try to see large 1 800 000 0000 number on front with large logo

Size bigger then standard business card

I like to integrate LAS VEGAS sign to one of sides

Target Market(s)

Handy man services, Home renovation and remodeling

Industry/Entity Type

Handyman

Contact Information for Business Card

Tidewell Works LLC.
Name: BORIS KELMANTOV
Phone "Temporary": 000 000 0000
Adress: 5172 Orchid Ln, Las Vegas NV 89147
Website: www.tidewellworks.vegas
Email: info@tidewellworks.vegas

Requirements
Must have
• Two side
• side n1: LOGO
• side n2: INFO
Nice to have
• Like to have some interesting idea for client to remember!
• With logo added to both side at different stile
Should not have
• Standard design,

```html
<!DOCTYPE html>
<html lang="en">
<head>
<meta charset="utf-8">
<title>Tidewell Works – Business Card</title>
<link href="https://fonts.googleapis.com/css2?family=Lato:wght@400;700;900&display=swap" rel="stylesheet">
<style>
  :root {
    --navy: #1c2b38;
    --orange: #e9a325;
    --sky: #8fc9ea;
    --white: #ffffff;
    --ink: #1f2d3a;
    --stage: #e6e8ea;
  }
  * { box-sizing: border-box; margin: 0; padding: 0; }
  html, body { width: 1200px; height: 880px; overflow: hidden; }
  body {
    background: var(--stage);
    font-family: "Lato", Arial, sans-serif;
    position: relative;
  }
  .card {
    position: absolute;
    width: 640px;
    height: 366px;
    border-radius: 22px;
    overflow: hidden;
    box-shadow: 0 14px 30px rgba(0,0,0,0.22);
  }

  /* Logo side */
  .card--logo {
    left: 110px; top: 40px;
    background: var(--navy);
    color: var(--white);
  }
  .logo-lockup {
    position: absolute;
    left: 110px; top: 110px;
    display: flex; align-items: center; gap: 22px;
  }
  .mascot--small {
    width: 86px; height: 146px;
    border-radius: 40px 40px 14px 14px;
    background: linear-gradient(180deg, var(--orange) 0 22%, var(--sky) 22% 48%, var(--orange) 48% 100%);
  }
  .brand-name {
    font-weight: 900;
    font-size: 50px;
    letter-spacing: 0.5px;
    line-height: 1;
  }
  .tagline {
    margin-top: 16px;
    font-size: 19px;
    letter-spacing: 1px;
    text-align: center;
    line-height: 1.3;
  }
  .tagline span { display: block; letter-spacing: 0.5px; text-transform: none; }

  /* Info side */
  .card--info {
    left: 450px; top: 474px;
    background: var(--white);
    color: var(--ink);
  }
  .card--info .brand-name {
    position: absolute;
    left: 40px; top: 96px;
    color: var(--navy);
    font-size: 46px;
  }
  .mascot--large {
    position: absolute;
    right: 70px; top: 34px;
    width: 170px; height: 262px;
    border-radius: 80px 80px 24px 24px;
    background: linear-gradient(180deg, var(--orange) 0 20%, var(--sky) 20% 46%, var(--orange) 46% 100%);
  }
  .holder-name {
    position: absolute;
    left: 40px; top: 178px;
    font-weight: 900;
    font-size: 22px;
    letter-spacing: 0.5px;
  }
  .address {
    position: absolute;
    left: 40px; top: 214px;
    font-size: 15px;
    line-height: 1.35;
  }
  .contact-list {
    position: absolute;
    left: 40px; top: 262px;
    list-style: none;
    font-size: 15px;
  }
  .contact-list li { display: flex; align-items: center; gap: 8px; height: 22px; }
  .contact-icon {
    width: 17px; height: 17px; border-radius: 50%;
    background: var(--orange);
    display: inline-flex; align-items: center; justify-content: center;
  }
  .info-band {
    position: absolute; left: 0; bottom: 0;
    width: 100%; height: 22px;
  }
</style>
</head>
<body>

  <section class="card card--logo">
    <div class="logo-lockup">
      <div class="mascot mascot--small" role="img" aria-label="Cartoon handyman mascot in orange cap and overalls giving a thumbs up"></div>
      <div>
        <div class="brand-name">Tidewell Works</div>
        <p class="tagline">ONE CALL WE DO IT ALL<span>We do it right</span></p>
      </div>
    </div>
  </section>

  <section class="card card--info">
    <div class="brand-name">Tidewell Works</div>
    <div class="mascot mascot--large" role="img" aria-label="Cartoon handyman mascot in orange cap and overalls holding a hammer, giving a thumbs up"></div>

    <div class="holder-name">BORIS KELMANTOV</div>
    <p class="address">5172 Orchid Ln,<br>Las Vegas NV 89147</p>

    <ul class="contact-list">
      <li>
        <span class="contact-icon">
          <svg width="10" height="10" viewBox="0 0 10 10"><path d="M2 1 L4 1 L4.6 3 L3.5 3.8 Q4.5 5.8 6.2 6.5 L7 5.4 L9 6 L9 8 Q5 9 2.5 6 Q0.8 3.5 2 1 Z" fill="#fff"/></svg>
        </span>000 000 0000
      </li>
      <li>
        <span class="contact-icon">
          <svg width="10" height="10" viewBox="0 0 10 10"><rect x="1" y="2.5" width="8" height="5.5" fill="#fff"/><path d="M1 2.5 L5 5.5 L9 2.5" stroke="#e9a325" stroke-width="0.9" fill="none"/></svg>
        </span>info@tidewellworks.vegas
      </li>
      <li>
        <span class="contact-icon">
          <svg width="10" height="10" viewBox="0 0 10 10"><circle cx="5" cy="5" r="3.8" fill="none" stroke="#fff" stroke-width="0.9"/><ellipse cx="5" cy="5" rx="1.6" ry="3.8" fill="none" stroke="#fff" stroke-width="0.8"/><line x1="1.2" y1="5" x2="8.8" y2="5" stroke="#fff" stroke-width="0.8"/></svg>
        </span>www.tidewellworks.vegas
      </li>
    </ul>

    <svg class="info-band" viewBox="0 0 640 22" preserveAspectRatio="none" aria-hidden="true">
      <rect x="0" y="0" width="640" height="22" fill="var(--orange)"/>
      <polygon points="470,0 640,0 640,22 460,22" fill="var(--navy)"/>
    </svg>
  </section>

</body>
</html>
```